Visitenkarten-Design für Süßigkeiten-Onlineshop
Zielgruppe
Ich werde einen Onlineshop betreiben und Süßigkeiten aus aller Welt verkaufen.
Aufgabenstellung
Mein Logo sollte drauf sein. Die Visitenkarte kann auch bisschen stylischer gestaltet werden. Aber da lasse ich mich auch gerne überraschen.
Man könnte vielleicht noch den Slogan- Süßigkeiten aus aller Welt-
Mein Name sollte drauf stehen,
Jonas Brettel
Lindauer Weg 14
41562 Dormagen
E-Mail info@zuckerfuchs-shop.de
Pixgram @zuckerfuchs.de
Freundesseite Zuckerfuchs
Clipzo @zuckerfuhcs.de

```html
<!DOCTYPE html>
<html lang="de">
<head>
<meta charset="utf-8">
<title>Zuckerfuchs – Visitenkarte</title>
<link rel="stylesheet" href="https://fonts.googleapis.com/css2?family=Poppins:wght@400;600;700&display=swap">
<style>
  :root {
    --teal: #7bbdc3;
    --ink: #3a3a3a;
    --paper: #ffffff;
    --stage: #e9e6e1;
  }
  * { margin: 0; padding: 0; box-sizing: border-box; }
  html, body {
    width: 1200px; height: 900px; overflow: hidden;
    background: var(--stage);
    font-family: "Poppins", sans-serif;
  }
  .stage {
    width: 1200px; height: 900px;
    display: flex; flex-direction: column; align-items: center; justify-content: center;
    gap: 40px;
  }
  .card {
    position: relative;
    width: 700px; height: 400px;
    box-shadow: 0 6px 18px rgba(0,0,0,.12);
    overflow: hidden;
  }

  /* shared brand lockup */
  .brand { display: flex; flex-direction: column; align-items: center; }
  .brand__mark { border-radius: 50%; background: var(--teal); }
  .brand__name {
    font-weight: 600; text-transform: uppercase; color: var(--ink); line-height: 1;
  }
  .brand__rule { height: 1.5px; background: var(--ink); }
  .brand__dots { display: flex; gap: 10px; align-items: center; }
  .brand__dot { width: 5px; height: 5px; border-radius: 50%; background: var(--ink); }
  .brand__dot--big { width: 8px; height: 8px; }

  /* front */
  .card--front { background: var(--paper); }
  .card--front .brand {
    position: absolute; left: 0; top: 0; width: 370px; height: 400px;
    justify-content: center; gap: 12px;
  }
  .card--front .brand__mark { width: 110px; height: 110px; margin-bottom: 10px; }
  .card--front .brand__name { font-size: 28px; letter-spacing: 5px; }
  .card--front .brand__rule { width: 280px; }

  .divider {
    position: absolute; left: 370px; top: 70px; width: 1.5px; height: 200px; background: var(--ink);
  }
  .name-band {
    position: absolute; left: 395px; top: 28px; right: 0; height: 44px;
    background: var(--teal);
    clip-path: polygon(0 0, 100% 0, 100% 100%, 0 100%, 14px 50%);
    display: flex; align-items: center; padding-left: 30px;
  }
  .name-band__text {
    color: #fff; font-weight: 700; font-size: 24px; letter-spacing: 1.5px; text-transform: uppercase;
  }
  .contact {
    position: absolute; left: 400px; top: 92px; list-style: none;
    font-size: 15px; color: var(--ink); line-height: 1.3;
  }
  .contact__item { display: flex; align-items: center; gap: 14px; margin-bottom: 6px; }
  .contact__icon { width: 20px; height: 20px; flex: none; }
  .contact__icon--plain {
    width: 18px; height: 18px; border: 2px solid var(--teal); border-radius: 50%; margin: 0 1px;
  }

  /* back */
  .card--back { background: var(--teal); }
  .card--back .brand {
    position: absolute; inset: 0; justify-content: center; gap: 14px;
  }
  .card--back .brand__mark { width: 150px; height: 150px; background: #fff; margin-bottom: 8px; }
  .card--back .brand__name { color: #fff; font-size: 42px; letter-spacing: 8px; }
  .card--back .brand__rule { width: 440px; background: #fff; }
  .card--back .brand__dot { background: #fff; }
</style>
</head>
<body>
<main class="stage">
  <section class="card card--front" aria-label="Visitenkarte Vorderseite">
    <div class="brand">
      <div class="brand__mark"></div>
      <div class="brand__rule"></div>
      <p class="brand__name">Zuckerfuchs</p>
      <div class="brand__rule"></div>
      <div class="brand__dots"><span class="brand__dot"></span><span class="brand__dot brand__dot--big"></span><span class="brand__dot"></span></div>
    </div>
    <div class="divider"></div>
    <div class="name-band"><h1 class="name-band__text">Jonas Brettel</h1></div>
    <ul class="contact">
      <li class="contact__item">
        <svg class="contact__icon" viewBox="0 0 20 20" aria-hidden="true"><path d="M10 1a6 6 0 0 0-6 6c0 4.5 6 12 6 12s6-7.5 6-12a6 6 0 0 0-6-6z" fill="var(--teal)"/><circle cx="10" cy="7" r="2.3" fill="#fff"/></svg>
        <span>Lindauer Weg 14<br>41562 Lindenfeld</span>
      </li>
      <li class="contact__item">
        <svg class="contact__icon" viewBox="0 0 20 20" aria-hidden="true"><path d="M5 2l3 4-2 2c1 2.5 3.5 5 6 6l2-2 4 3-2 3c-7 0-14-7-14-14z" fill="var(--teal)"/></svg>
        <span>015239876540</span>
      </li>
      <li class="contact__item"><span class="contact__icon contact__icon--plain"></span><span>Pixgram @zuckerfuchs.de</span></li>
      <li class="contact__item"><span class="contact__icon contact__icon--plain"></span><span>Freundesseite Zuckerfuchs</span></li>
      <li class="contact__item"><span class="contact__icon contact__icon--plain"></span><span>Clipzo @zuckerfuhcs.de</span></li>
    </ul>
  </section>

  <section class="card card--back" aria-label="Visitenkarte Rückseite">
    <div class="brand">
      <div class="brand__mark"></div>
      <div class="brand__rule"></div>
      <p class="brand__name">Zuckerfuchs</p>
      <div class="brand__rule"></div>
      <div class="brand__dots"><span class="brand__dot"></span><span class="brand__dot brand__dot--big"></span><span class="brand__dot"></span></div>
    </div>
  </section>
</main>
</body>
</html>
```